Business card for massage therapy company called Brook Fern Wellness

Need business card for massage therapy company called Brook Fern Wellness. Would like my logo on the front and the back of the card I have 3 options of logos and you can play with what looks better.

Would like this information displayed on the back of the card:

Marcus Ellery
Licensed Massage Therapist
321-555-0147
brookfern-example.com
brookfern_rest_

```html
<!DOCTYPE html>
<html lang="en">
<head>
<meta charset="utf-8">
<title>Brook Fern Wellness – Business Card</title>
<link rel="stylesheet" href="https://fonts.googleapis.com/css2?family=Arimo:wght@400;700&display=swap">
<style>
  :root {
    --page-bg: #dfe2d0;
    --sage: #848872;
    --sage-deep: #7d806c;
    --ink: #5f6253;
    --paper: #ffffff;
    --leaf-faint: #f4f4f3;
    --shadow: #5a5c4e;
  }
  * { box-sizing: border-box; margin: 0; padding: 0; }
  html, body {
    width: 1200px; height: 1200px; overflow: hidden;
    background: var(--page-bg);
    font-family: "Arimo", Arial, sans-serif;
  }
  .sheet { position: relative; width: 1200px; height: 1200px; }
  .card {
    position: absolute; left: 209px; width: 781px; height: 446px;
    overflow: hidden;
    box-shadow: 6px 7px 0 var(--shadow);
  }
  .card--front { top: 98px; background: var(--sage); }
  .card--back { top: 602px; background: var(--paper); }

  .leaf-wash { position: absolute; }
  .card--front .leaf-wash {
    left: 180px; top: 0; width: 480px; height: 446px;
    background: radial-gradient(ellipse at 55% 50%, var(--sage-deep) 0%, rgba(125,128,108,0.6) 45%, rgba(132,136,114,0) 75%);
  }
  .card--back .leaf-wash {
    left: 110px; top: 25px; width: 600px; height: 421px;
    background: radial-gradient(ellipse at 50% 55%, var(--leaf-faint) 0%, rgba(244,244,243,0.7) 45%, rgba(255,255,255,0) 75%);
  }

  .front-mark {
    position: absolute; left: 279px; top: 100px;
    width: 212px; height: 212px;
    border: 2px solid var(--paper); border-radius: 50%;
    display: flex; align-items: center; justify-content: center;
    text-align: center;
    color: var(--paper); font-size: 22px; line-height: 1.25; letter-spacing: 0.04em;
  }

  .back-brand {
    position: absolute; left: 470px; top: 62px; width: 280px;
    text-align: center;
    color: var(--ink); font-size: 28px; line-height: 1.2;
  }

  .person { position: absolute; left: 45px; top: 230px; color: var(--ink); }
  .person__name { font-size: 50px; font-weight: 400; letter-spacing: -0.01em; line-height: 1; }
  .person__role { font-size: 21px; margin-top: 6px; }

  .contact { position: absolute; left: 45px; top: 370px; color: var(--ink); font-size: 20px; line-height: 26px; }
  .social { position: absolute; left: 533px; top: 391px; color: var(--ink); font-size: 20px; }
</style>
</head>
<body>
<main class="sheet">
  <section class="card card--front">
    <div class="leaf-wash" role="img" aria-label="Faint large leaf sprig decoration"></div>
    <div class="front-mark">Brook Fern<br>Wellness</div>
  </section>

  <section class="card card--back">
    <div class="leaf-wash" role="img" aria-label="Faint large leaf sprig decoration"></div>
    <div class="back-brand">Brook Fern Wellness</div>
    <div class="person">
      <h1 class="person__name">Marcus Ellery</h1>
      <p class="person__role">Licensed Massage Therapist</p>
    </div>
    <div class="contact">
      <p>321-555-0147</p>
      <p>brookfern-example.com</p>
    </div>
    <p class="social">brookfern_rest_</p>
  </section>
</main>
</body>
</html>
```